Branding product image: TOMBEL (Golden Papaya) in Plastic Cup (Ready to Eat)

The product is sliced Fruit in Light syrup
Flavour: TOMBEL (Golden Papaya)
The temporary product name: TOMBEL
I want the product design to be something 'fun', 'natural', and 'colourful'
The design concept could be anything depends on your imagination, but it must be eye catchy and attractive.
Basically, I want you to be creative in designing the logo and the overall graphic design for the label.
The measurement is 20 cm (Length) x 6,5 cm (Height)
The target customers are young and health conscious audiences (10 years - 65 years old).
Create something different. Something extraordinary.
Brief summary about the fruit:
This fruit only grows in certain part of the world. It grows in mountain area that is in tropical climate. The fruit flesh has a yellowish-golden color. It has an extraordinary taste (unlike normal papaya) and it suits very well with any dishes from cold appetizer, white/ red meat, desserts, and cocktails.
I need a packaging design for Fruit Cup productThe product is sliced Fruit in Light syrup.There will be various flavours i.e. apple, lychee, peach, papaya, etc.However, you may design the product using one sample flavour (i.e. papaya) first, as the designs of other flavours could be adjusted afterwards.The temporary product name is: RICCANAI want the product design to be something 'fun', 'natural', and 'colourful'.The design concept could be anything depends on your imagination. Basically, I want you to be creative in designing the logo and the overall graphic design for the label. - Create something different. Something extraordinary -Additional:The measurement is 20cm (Length) x 5cm (Height).The target customers are young audiences (10 years - 35 years old).The product design must stand out in the supermarket shelf.It must be eye catchy and attractive.Thank you,Harold-PLEASE REFER TO DESIGN SAMPLE ATTACHED TO HAVE A BETTER UNDERSTANDING FOR THE PRODUCT CONCEPT- Added Wednesday, September 17, 2014
Project Deadline Extended Reason: Haven't found a good design. Added Friday, September 19, 2014
Project Deadline Extended Reason: Need more time for designers to finalize and perfect the design.Thank you,Harold Added Monday, September 29, 2014
Project Deadline Extended Reason: I haven't found a great design yet. Added Tuesday, February 24, 2015
Reason: Getting better designs now. Still Open to new ideas while refining the latest designs from some designers.
Please do your best in submitting other great designs!

```html
<!DOCTYPE html>
<html lang="en">
<head>
<meta charset="utf-8">
<title>TOMBEL Fruit Cup Labels</title>
<link rel="stylesheet" href="https://fonts.googleapis.com/css2?family=Fredoka:wght@600&display=swap">
<style>
  :root {
    --canvas: #f4f5f6;
    --label-base: #ffffff;
    --label-edge: #e3e6e8;
    --brand: #c8177a;
    --flavour-text: #ffffff;

    --lychee: #36aee4;
    --lychee-mid: #6cc6ee;
    --lychee-light: #a9def5;

    --apple: #c4d936;
    --apple-mid: #d6e46c;
    --apple-light: #e6eea1;

    --peach: #ee9c62;
    --peach-mid: #f3b88d;
    --peach-light: #f8d4b8;

    --papaya: #8656b3;
    --papaya-mid: #a47fc8;
    --papaya-light: #c6afdc;
  }

  * { box-sizing: border-box; margin: 0; padding: 0; }

  html, body {
    width: 1200px;
    height: 1000px;
    overflow: hidden;
    background: var(--canvas);
    font-family: "Fredoka", "Arial Rounded MT Bold", sans-serif;
  }

  .sheet {
    position: relative;
    width: 1200px;
    height: 1000px;
  }

  .label {
    position: absolute;
    background: var(--label-base);
    border: 1px solid var(--label-edge);
    border-radius: 4px;
    overflow: hidden;
  }

  .label--front-large { left: 220px; top: 200px; width: 365px; height: 345px; }
  .label--back-large  { left: 625px; top: 200px; width: 370px; height: 345px; }
  .label--apple       { left: 235px; top: 650px; width: 220px; height: 235px; }
  .label--peach       { left: 492px; top: 650px; width: 222px; height: 235px; }
  .label--papaya      { left: 748px; top: 650px; width: 220px; height: 235px; }

  .flavour-lychee { --tone: var(--lychee); --tone-mid: var(--lychee-mid); --tone-light: var(--lychee-light); }
  .flavour-apple  { --tone: var(--apple);  --tone-mid: var(--apple-mid);  --tone-light: var(--apple-light); }
  .flavour-peach  { --tone: var(--peach);  --tone-mid: var(--peach-mid);  --tone-light: var(--peach-light); }
  .flavour-papaya { --tone: var(--papaya); --tone-mid: var(--papaya-mid); --tone-light: var(--papaya-light); }

  .label__waves {
    position: absolute;
    inset: 0;
    width: 100%;
    height: 100%;
  }
  .wave-light { fill: var(--tone-light); }
  .wave-mid   { fill: var(--tone-mid); }
  .wave-main  { fill: var(--tone); }

  .brand-name {
    position: absolute;
    left: 0;
    right: 0;
    text-align: center;
    color: var(--brand);
    font-weight: 600;
    letter-spacing: 2px;
    line-height: 1;
  }
  .label--front-large .brand-name { top: 120px; font-size: 66px; }
  .label--small .brand-name      { top: 82px;  font-size: 40px; letter-spacing: 1px; }

  .flavour-name {
    position: absolute;
    left: 0;
    right: 0;
    text-align: center;
    color: var(--flavour-text);
    font-weight: 600;
    text-transform: uppercase;
    line-height: 1;
  }
  .label--front-large .flavour-name { top: 293px; font-size: 23px; letter-spacing: 0.5px; }
  .label--small .flavour-name      { top: 200px; font-size: 14px; }
</style>
</head>
<body>
<main class="sheet">

  <section class="label label--front-large flavour-lychee">
    <svg class="label__waves" viewBox="0 0 100 100" preserveAspectRatio="none" aria-hidden="true">
      <path class="wave-light" d="M0 26 Q50 20 100 25 L100 100 L0 100 Z"/>
      <path class="wave-mid" d="M0 33 Q50 27 100 32 L100 100 L0 100 Z"/>
      <path class="wave-main" d="M0 40 Q50 34 100 39 L100 100 L0 100 Z"/>
    </svg>
    <h1 class="brand-name">TOMBEL</h1>
    <p class="flavour-name">Lychee Flavour</p>
  </section>

  <section class="label label--back-large flavour-lychee">
    <svg class="label__waves" viewBox="0 0 100 100" preserveAspectRatio="none" aria-hidden="true">
      <path class="wave-light" d="M0 10 Q55 6 100 0 L100 100 L0 100 Z"/>
      <path class="wave-mid" d="M0 30 Q55 18 100 8 L100 100 L0 100 Z"/>
      <path class="wave-main" d="M0 55 Q55 38 100 24 L100 100 L0 100 Z"/>
    </svg>
  </section>

  <section class="label label--small label--apple flavour-apple">
    <svg class="label__waves" viewBox="0 0 100 100" preserveAspectRatio="none" aria-hidden="true">
      <path class="wave-light" d="M0 34 Q50 28 100 33 L100 100 L0 100 Z"/>
      <path class="wave-mid" d="M0 41 Q50 35 100 40 L100 100 L0 100 Z"/>
      <path class="wave-main" d="M0 48 Q50 42 100 47 L100 100 L0 100 Z"/>
    </svg>
    <h2 class="brand-name">TOMBEL</h2>
    <p class="flavour-name">Apple Flavour</p>
  </section>

  <section class="label label--small label--peach flavour-peach">
    <svg class="label__waves" viewBox="0 0 100 100" preserveAspectRatio="none" aria-hidden="true">
      <path class="wave-light" d="M0 34 Q50 28 100 33 L100 100 L0 100 Z"/>
      <path class="wave-mid" d="M0 41 Q50 35 100 40 L100 100 L0 100 Z"/>
      <path class="wave-main" d="M0 48 Q50 42 100 47 L100 100 L0 100 Z"/>
    </svg>
    <h2 class="brand-name">TOMBEL</h2>
    <p class="flavour-name">Peach Flavour</p>
  </section>

  <section class="label label--small label--papaya flavour-papaya">
    <svg class="label__waves" viewBox="0 0 100 100" preserveAspectRatio="none" aria-hidden="true">
      <path class="wave-light" d="M0 34 Q50 28 100 33 L100 100 L0 100 Z"/>
      <path class="wave-mid" d="M0 41 Q50 35 100 40 L100 100 L0 100 Z"/>
      <path class="wave-main" d="M0 48 Q50 42 100 47 L100 100 L0 100 Z"/>
    </svg>
    <h2 class="brand-name">TOMBEL</h2>
    <p class="flavour-name">Papaya Flavour</p>
  </section>

</main>
</body>
</html>
```